Lantern Path Collective

Re-design our website www.lanternpc.org
We are a non profit catering for adults, elderly, veterans and youth in impoverished neighborhoods to improve their digital access and help them improve their lives and better our community.

I need the text on home page to stay. Its the first message vsitors shd read when they arrive on our page.

Number of Pages Required

4 page

Font styles to use
Other font styles liked:
• color and font shd be like the image attched below.

```html
<!DOCTYPE html>
<html lang="en">
<head>
<meta charset="utf-8">
<title>Lantern Path Collective — Landing Page Design</title>
<link href="https://fonts.googleapis.com/css2?family=Poppins:wght@300;400;500;600;700&family=Quicksand:wght@400;500;600&display=swap" rel="stylesheet">
<style>
:root{
  --board:#6896b6;
  --navy:#1e2a5a;
  --orange:#f05a28;
  --amber:#f58220;
  --green:#3cb54a;
  --mist:#e9eef5;
  --ink:#4a4f5c;
  --muted:#7b8190;
  --news:#d9d9d9;
  --foot:#a3a3a3;
  --foot-dark:#8e8e8e;
  --white:#ffffff;
}
*{margin:0;padding:0;box-sizing:border-box}
html,body{width:779px;height:1200px;overflow:hidden}
body{background:var(--board);font-family:"Poppins",sans-serif;position:relative;color:var(--ink)}
.board-title{position:absolute;left:57px;top:64px;font-family:"Quicksand",sans-serif;font-weight:400;color:var(--white);font-size:50px;line-height:60px;letter-spacing:1px}
.board-brand{position:absolute;left:58px;top:1085px;display:flex;align-items:center;gap:10px;color:var(--white);font-weight:600;font-size:19px;line-height:22px}
.board-brand .dot{width:34px;height:34px;border-radius:50%;background:#9fc6e0}
.page{position:absolute;left:314px;top:19px;width:416px;height:1162px;background:var(--white);overflow:hidden}
.page *{position:absolute}
.page .flow, .page .flow *{position:static}
.btn{background:var(--orange);color:var(--white);border-radius:8px;font-size:3.6px;font-weight:600;display:flex;align-items:center;justify-content:center}
.t-nav{font-size:3.5px;color:var(--navy);top:56px}
.h-serif{font-family:"Quicksand",sans-serif;color:var(--navy);font-weight:500}
.small{font-size:3.3px;line-height:6px;color:var(--muted)}
.sq{display:block}
.social{width:8px;height:8px;border-radius:50%;background:var(--mist)}
.card{background:var(--white);border:0.5px solid #dfe3ea}
.card .img{left:0;top:0;width:100%;height:56px}
.card .ttl{left:9px;top:66px;font-size:5.3px;font-weight:600;color:var(--navy)}
.card .txt{left:9px;top:79px;width:64px}
.card .btn{left:9px;top:107px;width:42px;height:13px}
.svc{top:212px;width:85px;height:69px}
.svc .ico{left:12px;top:8px}
.svc .ttl{left:12px;top:29px;font-size:5.2px;color:var(--navy)}
.svc .rule{left:12px;top:38px;width:46px;height:0.6px;background:var(--orange)}
.svc .txt{left:12px;top:41px;width:64px}
.f-head{font-size:4.2px;font-weight:600;color:var(--white);top:1064px}
.f-link{font-size:3.2px;color:var(--white)}
</style>
</head>
<body>

<h1 class="board-title">Landing<br>Page<br>Design</h1>
<div class="board-brand"><span class="dot"></span><span>Lantern Path<br>Collective</span></div>

<main class="page">
  <!-- header -->
  <div style="left:0;top:0;width:416px;height:31px;background:var(--white)"></div>
  <div style="left:80px;top:10px;display:flex;align-items:center;gap:3px;font-size:5px;font-weight:700;color:var(--navy);line-height:5.5px">
    <span class="flow" style="display:block;width:7px;height:7px;border-radius:50%;background:#8ec0de"></span>
    <span class="flow">Lantern Path<br>Collective</span>
  </div>
  <svg style="left:183px;top:13px" width="6" height="6" viewBox="0 0 24 24"><path fill="var(--navy)" d="M6.6 10.8a15 15 0 0 0 6.6 6.6l2.2-2.2c.3-.3.7-.4 1-.2 1.1.4 2.3.6 3.6.6.6 0 1 .4 1 1V20c0 .6-.4 1-1 1A17 17 0 0 1 3 4c0-.6.4-1 1-1h3.5c.6 0 1 .4 1 1 0 1.3.2 2.5.6 3.6.1.3 0 .7-.2 1z"/></svg>
  <div style="left:192px;top:10px;font-size:3px;color:var(--muted)">Contact Us</div>
  <div style="left:192px;top:15px;font-size:3.4px;color:var(--navy)">(555) 014-2270</div>
  <div style="left:225px;top:10px;width:0.5px;height:11px;background:#ccd"></div>
  <svg style="left:232px;top:14px" width="6" height="4" viewBox="0 0 12 8"><rect width="12" height="8" rx="1" fill="var(--navy)"/><path d="M0 0l6 4 6-4" stroke="#fff" stroke-width="1" fill="none"/></svg>
  <div style="left:243px;top:10px;font-size:3px;color:var(--muted)">Send Email</div>
  <div style="left:243px;top:15px;font-size:3.4px;color:var(--navy)">hello@lanternpc.org</div>
  <span class="social" style="left:297px;top:12px"></span>
  <span class="social" style="left:307px;top:12px"></span>
  <span class="social" style="left:317px;top:12px"></span>
  <span class="social" style="left:327px;top:12px"></span>

  <!-- nav -->
  <div style="left:0;top:31px;width:416px;height:17px;background:var(--mist)"></div>
  <div style="left:79px;top:35px;width:21px;height:9px;border-radius:5px;background:var(--white)"></div>
  <div class="t-nav" style="left:85px;top:37px;font-weight:600">Home</div>
  <div class="t-nav" style="left:110px;top:37px">Get Connected</div>
  <div class="t-nav" style="left:151px;top:37px">e-Waste Services</div>
  <div class="t-nav" style="left:196px;top:37px">Our Impact</div>
  <div class="t-nav" style="left:231px;top:37px">About</div>
  <div class="t-nav" style="left:256px;top:37px">Contact</div>
  <div class="btn" style="left:296px;top:34px;width:40px;height:11px">Donate</div>

  <!-- hero -->
  <div role="img" aria-label="Photo of three children smiling at a laptop in a bright library" style="left:0;top:48px;width:416px;height:174px;background:linear-gradient(90deg,#f4f1ec 0%,#eee6da 35%,#d8c2a4 60%,#a87a4e 85%,#8a5a34 100%)"></div>
  <h2 class="h-serif" style="left:79px;top:77px;font-size:16px;line-height:17px;font-weight:500;color:#1a1a1a">Creating a Social<br>Impact with e-Waste</h2>
  <p style="left:79px;top:122px;font-size:5.8px;line-height:9px;color:#2a2a2a">By transforming Unwanted Technology<br>into Opportunities for People In-Need.</p>
  <div class="btn" style="left:79px;top:151px;width:42px;height:13px">Learn More</div>

  <!-- service strip -->
  <div style="left:38px;top:212px;width:340px;height:69px;box-shadow:0 2px 6px rgba(0,0,0,.08)"></div>
  <div class="svc" style="left:38px;background:var(--white)">
    <svg class="ico" width="14" height="14" viewBox="0 0 24 24" fill="none" stroke="var(--orange)" stroke-width="1.2"><circle cx="12" cy="10" r="6"/><path d="M9 17h6M10 20h4"/></svg>
    <div class="ttl">Affordable Technology</div><div class="rule"></div>
    <p class="small txt">Give Yourself the Tools to Easily Access Opportunities Online</p>
  </div>
  <div class="svc" style="left:123px;background:var(--mist)">
    <svg class="ico" width="14" height="14" viewBox="0 0 24 24" fill="none" stroke="#3a6fb0" stroke-width="1.2"><circle cx="12" cy="12" r="9"/><ellipse cx="12" cy="12" rx="4" ry="9"/><path d="M3 12h18"/></svg>
    <div class="ttl">Internet Access</div><div class="rule"></div>
    <p class="small txt">Access the Online Services You Want without Breaking the Bank</p>
  </div>
  <div class="svc" style="left:208px;background:var(--white)">
    <svg class="ico" width="14" height="14" viewBox="0 0 24 24" fill="none" stroke="var(--green)" stroke-width="1.2"><rect x="3" y="5" width="18" height="12"/><path d="M1 19h22M7 9h6M7 12h4"/></svg>
    <div class="ttl">Digital Literacy Training</div><div class="rule"></div>
    <p class="small txt">Start doing the things you want to do online</p>
  </div>
  <div class="svc" style="left:293px;background:var(--mist)">
    <svg class="ico" width="14" height="14" viewBox="0 0 24 24" fill="none" stroke="var(--navy)" stroke-width="1.2"><rect x="9" y="2" width="12" height="8" rx="1"/><rect x="3" y="10" width="12" height="9" rx="1"/><path d="M6 13h6M6 16h6"/></svg>
    <div class="ttl">Tech Support</div><div class="rule"></div>
    <p class="small txt">Reduce Lost Productivity and Get Technical Issues Resolved in Less Than One Business Day</p>
  </div>

  <!-- changing lives -->
  <div role="img" aria-label="Circular photo of students working on laptops in a classroom" style="left:80px;top:313px;width:112px;height:112px;border-radius:50%;background:radial-gradient(circle at 40% 40%,#c9d3dc,#6f7b86 70%,#3e4650)"></div>
  <div style="left:83px;top:317px;width:21px;height:21px;border-radius:50%;background:var(--green)"></div>
  <svg style="left:88px;top:322px" width="11" height="11" viewBox="0 0 24 24" fill="none" stroke="#fff" stroke-width="2"><path d="M12 21V11M12 11c0-5 4-7 8-7 0 5-3 7-8 7zM12 14c0-4-3-6-7-6 0 4 3 6 7 6z"/></svg>
  <h2 class="h-serif" style="left:211px;top:325px;font-size:11px;line-height:13.5px">We’re Changing Lives<br>with your Help</h2>
  <p class="small" style="left:211px;top:360px;width:122px">Lantern Path Collective is a nonprofit and social enterprise that creates equitable access to opportunity by providing devices, internet access, digital skills training, and tech support for low-income families, the homeless, and Veterans in our communities while at the same time, empowering businesses and organizations to do good by diverting technology from landfills to protect our planet.</p>
  <div class="btn" style="left:211px;top:406px;width:42px;height:13px">Learn More</div>

  <!-- bridging section -->
  <div style="left:0;top:457px;width:416px;height:117px;background:var(--mist)"></div>
  <h2 class="h-serif" style="left:79px;top:476px;font-size:11px;line-height:13px;color:#1e1e1e">Lantern Path<br>Collective’s support is limitless<br>to the community</h2>
  <p class="small" style="left:79px;top:525px;width:122px;color:#333">Being digitally literate is no longer a luxury, it is a must-have skill for everyone to manage information, communicate, manage money, and access support plus other government services. It has become an essential tool for modern-day citizenship and participation; no one can afford to be left behind.</p>
  <div role="img" aria-label="Photo of an older couple using a laptop together at home" style="left:248px;top:476px;width:88px;height:104px;background:linear-gradient(160deg,#e8e6e2,#b9a99a 55%,#5a4a40)"></div>
  <div role="img" aria-label="Photo of a mother and child looking at a laptop" style="left:220px;top:547px;width:57px;height:56px;background:linear-gradient(150deg,#d8cfc4,#8b6f5a 60%,#3f2f26)"></div>

  <!-- statistic quote -->
  <div style="left:79px;top:620px;width:22px;height:22px;border-radius:50%;background:var(--green)"></div>
  <div style="left:84px;top:621px;font-family:'Quicksand',sans-serif;font-size:15px;color:#fff;font-weight:600">“</div>
  <p style="left:110px;top:619px;font-size:7.4px;line-height:10px;color:var(--muted);font-family:'Quicksand',sans-serif;font-weight:500">Unfortunately, nearly <b style="position:static;color:var(--amber);font-family:'Poppins',sans-serif;font-size:10px;font-weight:700">100 million</b> Americans lack access<br>to a personal computer, internet connection, or both.</p>
  <p class="small" style="left:79px;top:654px;width:254px">This lack of access to digital technology creates a significant gap between the opportunities unconnected people can access and the ones digitally native households can. This gap in opportunities is known as the digital divide, and it’s our mission by joining hands with many other organizations that are tirelessly trying to shrink it because we believe that equitable access to information and technology empowers people to achieve their fullest potential.</p>
  <p class="small" style="left:79px;top:686px;width:254px">At the same time Electronic waste, or e-waste, refers to electronic products and components that are unwanted, unusable, or nearing the end of their useful life. While e-waste only makes up 2% of the mass in landfills, it accounts for 70% of toxic waste. Unfortunately, recycling is no longer a sufficient method for disposing of waste sustainably; given the scale of the climate crisis, reuse is now a prerequisite for protecting our planet.</p>

  <!-- explore -->
  <div style="left:0;top:726px;width:416px;height:132px;background:var(--mist)"></div>
  <h2 class="h-serif" style="left:0;top:747px;width:416px;text-align:center;font-size:8.4px;line-height:11px">Explore Opportunities Online with Low-Cost<br>Technology, Internet, Training &amp; Support</h2>
  <p class="small" style="left:104px;top:775px;width:208px;text-align:center;font-size:4px;line-height:7px;color:#333">In order to comprehensively shrink the digital divide, we offer you access to low-cost computers, low-cost internet, free digital literacy training and tech support. Click the boxes below to explore how we can help you and members of your community unlock their full potential through digital technology.</p>

  <div class="card" style="left:36px;top:826px;width:81px;height:132px">
    <div class="img" role="img" aria-label="Photo of a laptop on a wooden desk" style="background:linear-gradient(160deg,#d9d2c7,#7c6a58 60%,#3a2f27)"></div>
    <div class="ttl">Affordable Technology</div>
    <p class="small txt">By offering devices like desktop computers, laptops, tablets, and Wi-Fi hotspots through...</p>
    <div class="btn">Learn More</div>
  </div>
  <div class="card" style="left:124px;top:826px;width:81px;height:132px">
    <div class="img" role="img" aria-label="Photo of hands holding a phone with a glowing wifi symbol" style="background:linear-gradient(160deg,#3b3d63,#6d5e88 55%,#b49aa8)"></div>
    <div class="ttl">Internet Access</div>
    <p class="small txt">In the 21st century, having access to the internet is the same as having access to opportunity. That’s why...</p>
    <div class="btn">Learn More</div>
  </div>
  <div class="card" style="left:212px;top:826px;width:81px;height:132px">
    <div class="img" role="img" aria-label="Photo of a teacher helping students at a computer" style="background:linear-gradient(160deg,#8a6a58,#4a3a36 55%,#2a2630)"></div>
    <div class="ttl">Digital Literacy Training</div>
    <p class="small txt">Want to do things like help your children with online school, learn new career skills, apply for jobs...</p>
    <div class="btn">Learn More</div>
  </div>
  <div class="card" style="left:299px;top:826px;width:81px;height:132px">
    <div class="img" role="img" aria-label="Photo of a headset resting beside a desk phone" style="background:linear-gradient(160deg,#eef2f6,#b9c6d3 55%,#4b5663)"></div>
    <div class="ttl">Tech Support</div>
    <p class="small txt">We know that a device and the internet are only as valuable to someone as their ability ....</p>
    <div class="btn">Learn More</div>
  </div>

  <!-- newsletter -->
  <div style="left:0;top:979px;width:416px;height:53px;background:var(--news)"></div>
  <div style="left:76px;top:1002px;font-size:6.4px;font-weight:600;color:#111">Subscribe Newsletter</div>
  <div style="left:161px;top:997px;width:105px;height:19px;border-radius:10px;background:var(--white)"></div>
  <div style="left:169px;top:1004px;font-size:3.4px;color:#888">Email address</div>
  <div style="left:229px;top:999px;width:35px;height:14px;border-radius:8px;background:#0d0d0d;color:#fff;font-size:3.6px;font-weight:600;display:flex;align-items:center;justify-content:center">Subscribe</div>
  <span class="social" style="left:285px;top:1002px;width:10px;height:10px;background:#fff"></span>
  <span class="social" style="left:298px;top:1002px;width:10px;height:10px;background:#fff"></span>
  <span class="social" style="left:312px;top:1002px;width:10px;height:10px;background:#fff"></span>
  <span class="social" style="left:325px;top:1002px;width:10px;height:10px;background:#fff"></span>

  <!-- footer -->
  <div style="left:0;top:1032px;width:416px;height:110px;background:var(--foot)"></div>
  <div style="left:79px;top:1062px;display:flex;align-items:center;gap:3px;font-size:5.4px;font-weight:700;color:var(--white);line-height:6px">
    <span class="flow" style="display:block;width:8px;height:8px;border-radius:50%;background:#cfe3ef"></span>
    <span class="flow">Lantern Path<br>Collective</span>
  </div>
  <div style="left:79px;top:1101px;width:31px;height:12px;border-radius:6px;background:var(--white);color:#111;font-size:3.8px;font-weight:600;display:flex;align-items:center;justify-content:center">Donate</div>

  <div class="f-head" style="left:145px">Get Connected</div>
  <div class="f-link" style="left:145px;top:1075px">Get Technology</div>
  <div class="f-link" style="left:145px;top:1084px">Low-Cost Internet</div>
  <div class="f-link" style="left:145px;top:1093px">Digital Training</div>
  <div class="f-link" style="left:145px;top:1101px">Tech Support</div>
  <div class="f-link" style="left:145px;top:1110px">For Organizations</div>

  <div class="f-head" style="left:193px;line-height:5.5px">Repurpose<br>Your Tech</div>
  <div class="f-link" style="left:193px;top:1080px">E-Waste Services</div>
  <div class="f-link" style="left:193px;top:1089px">Data Destruction</div>
  <div class="f-link" style="left:193px;top:1098px">Technology Drives</div>

  <div class="f-head" style="left:239px">About Us</div>
  <div class="f-link" style="left:239px;top:1075px">About</div>
  <div class="f-link" style="left:239px;top:1084px">Our Impact</div>

  <div class="f-head" style="left:277px">Contact</div>
  <svg style="left:277px;top:1077px" width="4" height="4" viewBox="0 0 24 24"><path fill="#fff" d="M6.6 10.8a15 15 0 0 0 6.6 6.6l2.2-2.2c.3-.3.7-.4 1-.2 1.1.4 2.3.6 3.6.6.6 0 1 .4 1 1V20c0 .6-.4 1-1 1A17 17 0 0 1 3 4c0-.6.4-1 1-1h3.5c.6 0 1 .4 1 1 0 1.3.2 2.5.6 3.6.1.3 0 .7-.2 1z"/></svg>
  <div class="f-link" style="left:283px;top:1077px">(555) 014-2270</div>
  <svg style="left:277px;top:1091px" width="4" height="3" viewBox="0 0 12 8"><rect width="12" height="8" rx="1" fill="#fff"/></svg>
  <div class="f-link" style="left:283px;top:1090px">info@lanternpc.org</div>
  <svg style="left:277px;top:1102px" width="4" height="5" viewBox="0 0 12 16"><path fill="#fff" d="M6 0a6 6 0 0 0-6 6c0 4.5 6 10 6 10s6-5.5 6-10a6 6 0 0 0-6-6zm0 8.5A2.5 2.5 0 1 1 6 3.5a2.5 2.5 0 0 1 0 5z"/></svg>
  <div class="f-link" style="left:283px;top:1103px">418 Orchard Row, Fairhaven, CA 90099</div>

  <div style="left:0;top:1142px;width:416px;height:20px;background:var(--foot-dark)"></div>
  <div style="left:0;top:1149px;width:416px;text-align:center;font-size:3.2px;color:var(--white)">© 2023 by Lantern Path Collective. All rights reserved. | PRIVACY &amp; SECURITY POLICY</div>
</main>

</body>
</html>
```